Corvane Building Materials letterhead template

Simple but professional letterhead template for business communication.
LOGO/name in upper left, balanced by company contact info on right upper.
Subject description, date...
addressee, cc: and BC: if applicable editable info..

Need extra days to review

```html
<!DOCTYPE html>
<html lang="en">
<head>
<meta charset="UTF-8">
<title>Corvane Building Materials Letterhead</title>
<link rel="stylesheet" href="https://fonts.googleapis.com/css2?family=Montserrat:wght@700&display=swap">
<style>
  :root {
    --brand-blue: #2b5cb0;
    --paper: #ffffff;
  }
  html, body {
    margin: 0;
    padding: 0;
    overflow: hidden;
    background: var(--paper);
  }
  .letterhead {
    position: relative;
    width: 927px;
    height: 1200px;
    background: var(--paper);
    overflow: hidden;
    font-family: "Montserrat", Arial, sans-serif;
    font-weight: 700;
    color: var(--brand-blue);
  }
  .frame-lines {
    position: absolute;
    inset: 0;
    width: 927px;
    height: 1200px;
  }
  .brand {
    position: absolute;
    left: 82px;
    top: 85px;
    display: flex;
    align-items: center;
    gap: 18px;
  }
  .brand-mark {
    width: 90px;
    height: 90px;
    background: var(--brand-blue);
    border-radius: 14px;
  }
  .brand-name {
    margin: 0;
    font-size: 22px;
    line-height: 30px;
    letter-spacing: 1.5px;
    text-transform: uppercase;
  }
  .contact {
    position: absolute;
    left: 665px;
    top: 104px;
    font-size: 17px;
    line-height: 27px;
    font-style: normal;
  }
  .contact p { margin: 0; }
  .letter-fields {
    position: absolute;
    left: 82px;
    top: 304px;
    margin: 0;
    padding: 0;
    list-style: none;
    font-size: 15.5px;
    line-height: 20px;
  }
  .letter-fields li { margin-bottom: 16px; }
  .footer-address {
    position: absolute;
    left: 573px;
    top: 1143px;
    font-size: 17px;
    margin: 0;
  }
</style>
</head>
<body>
  <main class="letterhead">
    <svg class="frame-lines" viewBox="0 0 927 1200" aria-hidden="true">
      <line x1="485" y1="21" x2="927" y2="21" stroke="var(--brand-blue)" stroke-width="6"/>
      <line x1="458" y1="1105" x2="773" y2="1105" stroke="var(--brand-blue)" stroke-width="6"/>
      <path d="M461 1102 V1135 Q461 1195 530 1195 H927" fill="none" stroke="var(--brand-blue)" stroke-width="6"/>
    </svg>

    <header class="brand">
      <div class="brand-mark"></div>
      <h1 class="brand-name">Corvane<br>Building<br>Materials</h1>
    </header>

    <address class="contact">
      <p class="contact-phone">1-555-014-2270</p>
      <p class="contact-email">info@xyz-corvane.com</p>
    </address>

    <ul class="letter-fields">
      <li class="field-date">Date ..........................</li>
      <li class="field-subject">Subject ..........................</li>
      <li class="field-addressee">To ..........................</li>
      <li class="field-cc">CC ..........................</li>
      <li class="field-bcc">BCC ..........................</li>
    </ul>

    <p class="footer-address">Xyz Rd. Marlow, xyz 12345</p>
  </main>
</body>
</html>
```